Branding product image: TOMBEL (Golden Papaya) in Plastic Cup (Ready to Eat)

The product is sliced Fruit in Light syrup
Flavour: TOMBEL (Golden Papaya)
The temporary product name: TOMBEL
I want the product design to be something 'fun', 'natural', and 'colourful'
The design concept could be anything depends on your imagination, but it must be eye catchy and attractive.
Basically, I want you to be creative in designing the logo and the overall graphic design for the label.
The measurement is 20 cm (Length) x 6,5 cm (Height)
The target customers are young and health conscious audiences (10 years - 65 years old).
Create something different. Something extraordinary.
Brief summary about the fruit:
This fruit only grows in certain part of the world. It grows in mountain area that is in tropical climate. The fruit flesh has a yellowish-golden color. It has an extraordinary taste (unlike normal papaya) and it suits very well with any dishes from cold appetizer, white/ red meat, desserts, and cocktails.
I need a packaging design for Fruit Cup productThe product is sliced Fruit in Light syrup.There will be various flavours i.e. apple, lychee, peach, papaya, etc.However, you may design the product using one sample flavour (i.e. papaya) first, as the designs of other flavours could be adjusted afterwards.The temporary product name is: RICCANAI want the product design to be something 'fun', 'natural', and 'colourful'.The design concept could be anything depends on your imagination. Basically, I want you to be creative in designing the logo and the overall graphic design for the label. - Create something different. Something extraordinary -Additional:The measurement is 20cm (Length) x 5cm (Height).The target customers are young audiences (10 years - 35 years old).The product design must stand out in the supermarket shelf.It must be eye catchy and attractive.Thank you,Harold-PLEASE REFER TO DESIGN SAMPLE ATTACHED TO HAVE A BETTER UNDERSTANDING FOR THE PRODUCT CONCEPT- Added Wednesday, September 17, 2014
Project Deadline Extended Reason: Haven't found a good design. Added Friday, September 19, 2014
Project Deadline Extended Reason: Need more time for designers to finalize and perfect the design.Thank you,Harold Added Monday, September 29, 2014
Project Deadline Extended Reason: I haven't found a great design yet. Added Tuesday, February 24, 2015
Reason: Getting better designs now. Still Open to new ideas while refining the latest designs from some designers.
Please do your best in submitting other great designs!

```html
<!DOCTYPE html>
<html lang="en">
<head>
<meta charset="utf-8">
<title>Lupedos Golden Papaya – Cup Label</title>
<link rel="stylesheet" href="https://fonts.googleapis.com/css2?family=Nunito:wght@800&family=Dancing+Script:wght@600&display=swap">
<style>
  :root {
    --bg: #262626;
    --label-white: #ffffff;
    --brand-green: #6e7d10;
    --band-green-dark: #6a7c0e;
    --band-green-light: #9aab2a;
    --gold-dark: #c4a000;
    --gold-light: #ecd23a;
    --orange: #f39a1e;
    --pale-yellow: #fbeb9a;
    --syrup-text: #5a4a00;
    --fruit-green: #7ea52c;
    --fruit-orange: #f2a43a;
  }
  html, body {
    margin: 0;
    width: 806px;
    height: 1200px;
    overflow: hidden;
    background: var(--bg);
  }
  .label {
    position: absolute;
    left: 70px;
    top: 409px;
    width: 665px;
    height: 382px;
    background: var(--label-white);
    overflow: hidden;
  }
  .label-art {
    position: absolute;
    inset: 0;
  }
  .brand-name {
    position: absolute;
    left: 16px;
    top: 18px;
    margin: 0;
    font-family: "Nunito", sans-serif;
    font-weight: 800;
    font-size: 80px;
    line-height: 1;
    color: var(--brand-green);
    letter-spacing: 0.5px;
  }
  .flavour-box {
    position: absolute;
    left: 27px;
    top: 152px;
    width: 220px;
    height: 172px;
    border-radius: 10px;
    background: linear-gradient(135deg, var(--gold-light), var(--gold-dark));
    text-align: center;
  }
  .flavour-name {
    margin: 22px 0 0;
    font-family: "Nunito", sans-serif;
    font-weight: 800;
    font-size: 44px;
    line-height: 48px;
    color: var(--label-white);
  }
  .flavour-syrup {
    margin: 8px 0 0;
    font-family: "Dancing Script", cursive;
    font-weight: 600;
    font-size: 21px;
    color: var(--syrup-text);
  }
  .fruit-photo {
    position: absolute;
    left: 266px;
    top: 166px;
    width: 356px;
    height: 190px;
    border-radius: 40px;
    background: linear-gradient(100deg, var(--fruit-green) 0%, var(--fruit-green) 30%, var(--fruit-orange) 60%, var(--orange) 100%);
  }
</style>
</head>
<body>
  <section class="label">
    <svg class="label-art" width="665" height="382" viewBox="0 0 665 382" aria-hidden="true">
      <defs>
        <linearGradient id="bandGreen" x1="0" y1="0" x2="1" y2="0">
          <stop offset="0" stop-color="#6a7c0e"/>
          <stop offset="1" stop-color="#9aab2a"/>
        </linearGradient>
        <linearGradient id="paleSweep" x1="0" y1="0" x2="1" y2="0">
          <stop offset="0" stop-color="#ffffff"/>
          <stop offset="1" stop-color="#fbeb9a"/>
        </linearGradient>
      </defs>
      <path class="sweep-pale" d="M470 0 H665 V230 C600 200 560 120 470 0 Z" fill="url(#paleSweep)"/>
      <path class="sweep-gold" d="M560 0 H665 V200 C630 150 600 80 560 0 Z" fill="#ecd23a" opacity="0.7"/>
      <path class="sweep-orange" d="M250 330 C420 300 560 250 665 150 V260 C560 300 420 320 250 330 Z" fill="#f39a1e"/>
      <path class="band-green" d="M0 330 C220 325 460 300 665 225 V382 H0 Z" fill="url(#bandGreen)"/>
      <path class="band-line" d="M0 336 C240 330 470 305 665 235" fill="none" stroke="#ffffff" stroke-opacity="0.5" stroke-width="1.5"/>
    </svg>

    <h1 class="brand-name">Lupedos</h1>

    <div class="flavour-box">
      <p class="flavour-name">Golden<br>Papaya</p>
      <p class="flavour-syrup">in Light Syrup</p>
    </div>

    <div class="fruit-photo" role="img" aria-label="Photo of a whole green papaya beside a halved ripe papaya with black seeds and a water splash"></div>
  </section>
</body>
</html>
```